Boutique personal training and fitness studio - banner ad design

We need a 'revolving' banner ad designed for our personal training and fitness studio. There are three separate offers (i.e. 3 pages to the advertisements)
Offer 1
PT Starter Pack
3 personal training sessions
$119
New clients only
Offer 2
Group fitness
2 weeks unlimited group fitness classes
$29
New clients only
Offer 3
Strength starter pack
2 weeks unlimited group fitness classes and 2 PT sessions
$89
New clients only
Please do not put the words "Offer 1, 2 or 3" in the ads - just the text following each offer.
Each advertisement should be sized to fit across around half of the webpage and be in landscape format.
Each advertisement should have a suitable picture (no cartoons) and should be complimentary to the existing website.
Each advertisement should also include the logo (attached)
www.corrabankliftworks.com.au
Training

```html
<!DOCTYPE html>
<html lang="en">
<head>
<meta charset="utf-8">
<title>PT Starter Pack – Corrabank Liftworks</title>
<link rel="stylesheet" href="https://fonts.googleapis.com/css2?family=Ubuntu:wght@400;700&display=swap">
<style>
  :root {
    --brand-yellow: #fff200;
    --brand-black: #0a0a0a;
    --brand-white: #ffffff;
    --photo-dark: #2a2724;
    --photo-mid: #6b5a4a;
    --photo-warm: #c89a74;
  }
  html, body {
    margin: 0;
    padding: 0;
    overflow: hidden;
    background: #ffffff;
  }
  .banner {
    position: relative;
    width: 1200px;
    height: 375px;
    overflow: hidden;
    background: var(--brand-yellow);
    font-family: "Ubuntu", sans-serif;
  }
  .banner__shapes {
    position: absolute;
    inset: 0;
    width: 1200px;
    height: 375px;
  }
  .banner__title {
    position: absolute;
    left: 60px;
    top: 46px;
    margin: 0;
    font-weight: 700;
    font-size: 66px;
    line-height: 1;
    color: var(--brand-black);
    letter-spacing: -0.5px;
  }
  .banner__subtitle {
    position: absolute;
    left: 60px;
    top: 148px;
    margin: 0;
    font-weight: 400;
    font-size: 45px;
    line-height: 1;
    color: var(--brand-black);
  }
  .studio-name {
    position: absolute;
    left: 38px;
    top: 283px;
    display: flex;
    align-items: center;
    gap: 10px;
    font-weight: 700;
    font-size: 21px;
    line-height: 1.05;
    color: var(--brand-white);
    text-transform: uppercase;
    width: 200px;
  }
  .studio-name__dot {
    flex: none;
    width: 16px;
    height: 16px;
    border-radius: 50%;
    background: var(--brand-white);
  }
  .price {
    position: absolute;
    left: 340px;
    top: 258px;
    color: var(--brand-yellow);
  }
  .price__amount {
    display: block;
    font-weight: 400;
    font-size: 74px;
    line-height: 1;
  }
  .price__note {
    display: block;
    margin-top: 2px;
    font-weight: 400;
    font-size: 25px;
    line-height: 1;
  }
</style>
</head>
<body>
  <div class="banner">
    <svg class="banner__shapes" viewBox="0 0 1200 375" aria-hidden="false">
      <defs>
        <linearGradient id="photo-tones" x1="0" y1="0" x2="1" y2="1">
          <stop offset="0" stop-color="var(--photo-dark)"/>
          <stop offset="0.45" stop-color="var(--photo-mid)"/>
          <stop offset="0.7" stop-color="var(--photo-warm)"/>
          <stop offset="1" stop-color="var(--photo-dark)"/>
        </linearGradient>
      </defs>

      <!-- bottom black band -->
      <polygon class="band-black" points="0,245 668,245 640,375 0,375" fill="var(--brand-black)"/>

      <!-- photo area -->
      <polygon class="photo-area" role="img"
        aria-label="Photo: smiling woman in a yellow tank top training on a shoulder press machine in the gym"
        points="722,0 1200,0 1200,375 640,375" fill="url(#photo-tones)"/>

      <!-- checkered accents along the seam -->
      <polygon class="accent-black" points="655,40 700,40 694,62 649,62" fill="var(--brand-black)"/>
      <polygon class="accent-black" points="700,62 716,62 711,84 695,84" fill="var(--brand-black)"/>
      <polygon class="accent-black" points="618,62 649,62 644,84 613,84" fill="var(--brand-black)"/>
      <polygon class="accent-black" points="672,220 700,220 695,245 668,245" fill="var(--brand-black)"/>
      <polygon class="accent-yellow" points="650,290 676,290 670,318 644,318" fill="var(--brand-yellow)"/>
      <polygon class="accent-yellow" points="640,318 660,318 654,346 634,346" fill="var(--brand-yellow)"/>
      <polygon class="accent-yellow" points="660,346 682,346 676,375 654,375" fill="var(--brand-yellow)"/>
    </svg>

    <h1 class="banner__title">PT Starter Pack</h1>
    <p class="banner__subtitle">3 personal training sessions</p>

    <div class="studio-name">
      <span class="studio-name__dot"></span>
      <span>Corrabank Liftworks</span>
    </div>

    <div class="price">
      <span class="price__amount">$119</span>
      <span class="price__note">New clients only</span>
    </div>
  </div>
</body>
</html>
```